IT support company needs Banner Ad for the top of their quote layout template

We need a banner Ad for the top of our for quote layout template so it is sent out on all our quotes

The banner size must be 827 x 100 pixels - anything larger than 60 KB can cause upload time issues

We have attached our logo and examples of the quote page to see how it looks in the context of the whole page.

Essential elements of the banner
- Must have our logo but this can be changed to be different colours if it makes the design work better i.e. Tidal Grove could be all in white

Colours
- Can use all of our standard colours - Orange, Black, Grey and White

Images
- As a premium IT support company we deal with people and technology so would like to see both of these Incorporated into the banner i.e. people using technology These images could be watermarked or one colour effect.

Look and Feel
- Professional, friendly, people, technology, premium

Target Market
Small business owners and managers

Industry/Entity Type

It Company

```html
<!DOCTYPE html>
<html lang="en">
<head>
<meta charset="UTF-8">
<title>Tidal Grove – Quote Banner Options</title>
<link rel="stylesheet" href="https://fonts.googleapis.com/css2?family=Montserrat:wght@700&family=Open+Sans:wght@400&display=swap">
<style>
  :root {
    --orange: #f7770f;
    --black: #1c1c1c;
    --white: #ffffff;
    --grey: #5d5e63;
    --page: #e4e5e7;
    --office-dark: #3e4045;
    --office-mid: #8d8983;
    --office-light: #ece9e6;
    --office-warm: #e98a2c;
    --network-dark: #35363a;
    --network-light: #d9dadc;
  }
  * { margin: 0; padding: 0; box-sizing: border-box; }
  html, body { width: 1200px; height: 1200px; overflow: hidden; }
  body { background: var(--page); position: relative; }

  .banner {
    position: absolute;
    left: 106px;
    width: 991px;
    height: 120px;
    overflow: hidden;
    background: var(--white);
  }
  .banner--rounded { top: 240px; }
  .banner--square  { top: 542px; }
  .banner--network { top: 848px; }

  .accent-strip {
    position: absolute; top: 0; bottom: 0; left: 0;
    width: 19px; background: var(--orange);
  }
  .accent-strip--right { left: auto; right: 0; width: 29px; }
  .banner--square .accent-strip,
  .banner--network .accent-strip { width: 14px; }

  .photo {
    position: absolute; top: 0; bottom: 0; right: 0;
  }
  .photo--office {
    background:
      radial-gradient(ellipse 70px 80px at 38% 55%, rgba(246,244,242,0.95), rgba(246,244,242,0) 100%),
      radial-gradient(ellipse 60px 70px at 27% 60%, rgba(240,238,236,0.9), rgba(240,238,236,0) 100%),
      radial-gradient(circle 22px at 57% 55%, rgba(255,168,70,0.95), rgba(255,168,70,0) 100%),
      radial-gradient(circle 14px at 73% 35%, rgba(255,240,220,0.9), rgba(255,240,220,0) 100%),
      radial-gradient(circle 14px at 85% 30%, rgba(255,240,220,0.9), rgba(255,240,220,0) 100%),
      radial-gradient(ellipse 120px 90px at 70% 80%, rgba(233,138,44,0.35), rgba(233,138,44,0) 100%),
      linear-gradient(180deg, rgba(0,0,0,0.15) 0%, rgba(0,0,0,0) 40%, rgba(0,0,0,0.1) 100%),
      linear-gradient(90deg, var(--office-dark) 0%, #6b6a6a 14%, var(--office-mid) 30%, #9a958f 44%, #6f6a64 48%, #a78666 58%, #c9b9a8 72%, var(--office-light) 88%, #cfcac4 100%);
  }
  .photo--network {
    background:
      radial-gradient(ellipse 110px 70px at 22% 30%, rgba(235,236,238,0.75), rgba(235,236,238,0) 100%),
      radial-gradient(ellipse 70px 90px at 40% 55%, rgba(30,30,34,0.55), rgba(30,30,34,0) 100%),
      radial-gradient(ellipse 60px 80px at 52% 60%, rgba(220,218,214,0.7), rgba(220,218,214,0) 100%),
      linear-gradient(90deg, var(--network-dark) 0%, #77787c 12%, var(--network-light) 30%, #a9aaad 48%, #7a7b80 62%, var(--grey) 64%, var(--grey) 100%);
  }
  .banner--rounded .photo { left: 300px; right: 29px; }
  .banner--square .photo,
  .banner--network .photo { left: 333px; }

  .logo-panel {
    position: absolute; top: 0; bottom: 0; left: 19px;
    width: 331px; background: var(--white);
    border-radius: 0 90px 90px 0 / 0 60px 60px 0;
    display: flex; align-items: center; padding-left: 27px;
  }
  .banner--square .logo-panel,
  .banner--network .logo-panel {
    left: 14px; width: 319px; border-radius: 0; padding-left: 32px;
  }

  .brand-name {
    font-family: "Montserrat", sans-serif;
    font-weight: 700;
    font-size: 30px;
    letter-spacing: 1px;
    text-transform: uppercase;
    color: var(--black);
    white-space: nowrap;
  }

  .cta {
    position: absolute;
    left: 773px; top: 58px;
    width: 205px; height: 44px;
    background: var(--white);
    clip-path: polygon(10px 0, 100% 0, calc(100% - 10px) 100%, 0 100%);
    display: flex; align-items: center; justify-content: center;
    font-family: "Open Sans", sans-serif;
    font-size: 31px;
    line-height: 1;
    color: var(--orange);
  }
</style>
</head>
<body>

  <section class="banner banner--rounded">
    <div class="accent-strip"></div>
    <div class="photo photo--office" role="img" aria-label="Two colleagues smiling at a laptop in a modern office with warm pendant lights"></div>
    <div class="accent-strip accent-strip--right"></div>
    <div class="logo-panel"><span class="brand-name">Tidal Grove</span></div>
    <div class="cta">start</div>
  </section>

  <section class="banner banner--square">
    <div class="accent-strip"></div>
    <div class="photo photo--office" role="img" aria-label="Two colleagues smiling at a laptop in a modern office with warm pendant lights"></div>
    <div class="logo-panel"><span class="brand-name">Tidal Grove</span></div>
    <div class="cta">start</div>
  </section>

  <section class="banner banner--network">
    <div class="accent-strip"></div>
    <div class="photo photo--network" role="img" aria-label="Business team looking at a glowing network of connected icons, in grey tones"></div>
    <div class="logo-panel"><span class="brand-name">Tidal Grove</span></div>
    <div class="cta">start</div>
  </section>

</body>
</html>
```